Cyber Security Company Services Graphic

We need a 3D graphic of our services that resembles a great graphic that is used by another company. The image will be used on web sites, in presentations, and collateral. We will need to modify the text at some point as we change the name of the services. The attached file has the content that needs to be in our graphic (rough layout) and the example of a great graphic that we are using as the baseline for our image.

```html
<!DOCTYPE html>
<html lang="en">
<head>
<meta charset="utf-8">
<title>Corvane Services Stack</title>
<link href="https://fonts.googleapis.com/css2?family=Lato:wght@300;400&display=swap" rel="stylesheet">
<style>
  :root {
    --navy: #1e2640;
    --navy-top: #2c3452;
    --seam: #1a2138;
    --orange: #d9480f;
    --orange-top: #ff5a1f;
    --blue: #234f7b;
    --blue-top: #305c8a;
    --grey: #9d9dab;
    --grey-top: #bcbdc8;
    --label: #4a4f5c;
    --line: #c4c6cc;
    --page: #ffffff;
  }
  html, body {
    margin: 0;
    width: 1152px;
    height: 1200px;
    overflow: hidden;
    background: var(--page);
    font-family: "Lato", sans-serif;
  }
  .services-stack {
    position: absolute;
    top: 294px;
    left: 0;
    width: 1152px;
    height: 612px;
  }
  .tier-label { fill: #fff; font-family: "Lato", sans-serif; font-weight: 400; text-anchor: middle; }
  .base-label { font-size: 38px; font-weight: 300; }
  .mid-label { font-size: 27px; font-weight: 300; }
  .block-label { font-size: 17px; }
  .node-label { fill: var(--label); font-family: "Lato", sans-serif; font-size: 15px; }
  .node-label.left { text-anchor: end; }
  .node { fill: #fff; stroke: #e6e7ea; stroke-width: 1; filter: url(#nodeShadow); }
  .connector { stroke: var(--line); stroke-width: 1.2; stroke-dasharray: 3 4; }
  .glass { fill: url(#glassFill); }
  .icon-orange { fill: none; stroke: var(--orange-top); stroke-width: 1.8; }
  .icon-blue { fill: none; stroke: var(--blue); stroke-width: 1.8; }
  .icon-grey { fill: none; stroke: #8a8b98; stroke-width: 1.8; }
</style>
</head>
<body>
<svg class="services-stack" viewBox="0 40 1882 1000" xmlns="http://www.w3.org/2000/svg">
  <defs>
    <linearGradient id="skyFill" x1="0" y1="0" x2="0" y2="1">
      <stop offset="0" stop-color="#ffffff"/>
      <stop offset="1" stop-color="#f0f0f2"/>
    </linearGradient>
    <linearGradient id="glassFill" x1="0" y1="0" x2="0" y2="1">
      <stop offset="0" stop-color="#ffffff" stop-opacity="0"/>
      <stop offset="1" stop-color="#ffffff" stop-opacity="0.9"/>
    </linearGradient>
    <filter id="nodeShadow" x="-50%" y="-50%" width="200%" height="200%">
      <feDropShadow dx="0" dy="2" stdDeviation="2.5" flood-color="#000" flood-opacity="0.12"/>
    </filter>
    <filter id="baseShadow" x="-10%" y="-50%" width="120%" height="200%">
      <feGaussianBlur stdDeviation="8"/>
    </filter>
  </defs>

  <rect class="cloud-backdrop" role="img" aria-label="Soft white clouds behind the service stack" x="0" y="40" width="1882" height="905" fill="url(#skyFill)"/>

  <g class="column column-vulnerability">
    <rect class="glass" x="615" y="330" width="190" height="300" rx="20"/>
    <ellipse cx="708" cy="632" rx="62" ry="6" fill="#b83a0a"/>
    <line class="connector" x1="708" y1="358" x2="708" y2="632"/>
    <circle class="node" cx="708" cy="358" r="22"/>
    <path class="icon-orange" d="M698 360 a10 8 0 0 1 20 0 z M708 360 v8 a2 2 0 0 1 -4 0"/>
    <text class="node-label" x="740" y="355">Human</text>
    <text class="node-label" x="740" y="373">Behavior</text>
    <circle class="node" cx="708" cy="428" r="22"/>
    <circle class="icon-orange" cx="708" cy="428" r="6"/><circle cx="708" cy="428" r="2" fill="var(--orange-top)"/>
    <text class="node-label left" x="673" y="424">Threat</text>
    <text class="node-label left" x="673" y="442">Hunting</text>
    <circle class="node" cx="708" cy="496" r="22"/>
    <path class="icon-orange" d="M699 492 h10 v8 h-10 z M711 502 l8 -10"/>
    <text class="node-label" x="740" y="493">Vulnerability</text>
    <text class="node-label" x="740" y="511">Assessment</text>
    <circle class="node" cx="708" cy="565" r="22"/>
    <circle class="icon-orange" cx="708" cy="565" r="6" stroke-dasharray="3 2"/>
    <text class="node-label left" x="675" y="561">Vulnerability</text>
    <text class="node-label left" x="675" y="579">Management</text>
  </g>

  <g class="column column-detection">
    <rect class="glass" x="870" y="330" width="188" height="300" rx="20"/>
    <ellipse cx="963" cy="632" rx="62" ry="6" fill="#1b3e63"/>
    <line class="connector" x1="963" y1="358" x2="963" y2="632"/>
    <circle class="node" cx="963" cy="358" r="22"/>
    <path class="icon-blue" d="M963 348 l8 3 v6 c0 6 -4 9 -8 11 c-4 -2 -8 -5 -8 -11 v-6 z"/>
    <text class="node-label" x="992" y="354">Endpoint</text>
    <text class="node-label" x="992" y="372">Protection</text>
    <circle class="node" cx="963" cy="428" r="22"/>
    <path class="icon-blue" d="M959 418 h8 v6 h-8 z M963 424 v4 M955 428 h16 M955 428 v4 M963 428 v4 M971 428 v4"/>
    <circle class="icon-blue" cx="955" cy="435" r="2.5"/><circle class="icon-blue" cx="963" cy="435" r="2.5"/><circle class="icon-blue" cx="971" cy="435" r="2.5"/>
    <text class="node-label left" x="932" y="424">Networks</text>
    <text class="node-label left" x="932" y="442">&amp; Servers</text>
    <circle class="node" cx="963" cy="496" r="22"/>
    <path class="icon-blue" d="M953 502 a5 5 0 0 1 1 -10 a7 7 0 0 1 13 -1 a5 5 0 0 1 2 11 z"/>
    <text class="node-label" x="992" y="503">Cloud</text>
    <circle class="node" cx="963" cy="565" r="22"/>
    <circle class="icon-blue" cx="963" cy="565" r="8"/><path class="icon-blue" d="M963 560 v5 h4"/>
    <text class="node-label left" x="936" y="570">24x7 SOC</text>
  </g>

  <g class="column column-governance">
    <rect class="glass" x="1125" y="330" width="188" height="300" rx="20"/>
    <ellipse cx="1219" cy="632" rx="62" ry="6" fill="#7f808e"/>
    <line class="connector" x1="1219" y1="358" x2="1219" y2="632"/>
    <circle class="node" cx="1219" cy="358" r="22"/>
    <path class="icon-grey" d="M1212 351 h14 v14 h-14 z M1216 355 h6 v6 h-6 z M1209 355 h3 M1209 361 h3 M1226 355 h3 M1226 361 h3"/>
    <text class="node-label" x="1248" y="363">Technology</text>
    <circle class="node" cx="1219" cy="428" r="22"/>
    <circle class="icon-blue" cx="1212" cy="424" r="3"/><circle class="icon-blue" cx="1226" cy="424" r="3"/>
    <path class="icon-blue" d="M1206 434 a6 5 0 0 1 12 0 M1220 434 a6 5 0 0 1 12 0"/>
    <text class="node-label left" x="1189" y="433">People</text>
    <circle class="node" cx="1219" cy="496" r="22"/>
    <path class="icon-grey" d="M1211 491 h16 M1211 496 h16 M1211 501 h16"/>
    <text class="node-label" x="1250" y="501">Process</text>
    <circle class="node" cx="1219" cy="565" r="22"/>
    <text class="node-label left" x="1189" y="563">Cyber</text>
    <text class="node-label left" x="1189" y="581">Insurance</text>
  </g>

  <!-- base platform -->
  <ellipse cx="965" cy="998" rx="800" ry="10" fill="#000" opacity="0.25" filter="url(#baseShadow)"/>
  <polygon points="175,920 340,872 1590,872 1755,920" fill="var(--navy-top)"/>
  <rect x="175" y="920" width="1580" height="75" fill="var(--navy)"/>
  <text class="tier-label base-label" x="965" y="973">Corvane Portal &amp; Operating System</text>

  <!-- service delivery tier -->
  <g class="tier-delivery">
    <polygon points="340,815 448,788 1482,788 1590,815 1590,881 340,881" fill="var(--seam)"/>
    <polygon points="340,815 448,788 670,788 640,815" fill="var(--orange-top)"/>
    <polygon points="648,815 678,788 960,788 960,815" fill="var(--orange-top)"/>
    <polygon points="968,815 968,788 1250,788 1280,815" fill="var(--blue-top)"/>
    <polygon points="1288,815 1258,788 1482,788 1590,815" fill="var(--blue-top)"/>
    <rect x="340" y="815" width="300" height="66" fill="var(--orange)"/>
    <rect x="648" y="815" width="312" height="66" fill="var(--orange)"/>
    <rect x="968" y="815" width="312" height="66" fill="var(--blue)"/>
    <rect x="1288" y="815" width="302" height="66" fill="var(--blue)"/>
    <text class="tier-label block-label" x="480" y="854">Consulting &amp; Advisory</text>
    <text class="tier-label block-label" x="786" y="854">Marketing &amp; Sales</text>
    <text class="tier-label block-label" x="1126" y="854">Reports &amp; Compliance</text>
    <text class="tier-label block-label" x="1440" y="854">Reports &amp; Compliance</text>
  </g>

  <!-- managed services tier -->
  <polygon points="448,733 540,713 1388,713 1482,733" fill="var(--navy-top)"/>
  <rect x="448" y="733" width="1034" height="55" fill="var(--navy)"/>
  <text class="tier-label mid-label" x="985" y="770">Managed Security Services</text>

  <!-- core services tier -->
  <g class="tier-core">
    <polygon points="540,650 615,625 1310,625 1388,650 1388,714 540,714" fill="var(--seam)"/>
    <polygon points="540,650 615,625 840,625 810,650" fill="var(--orange-top)"/>
    <polygon points="830,650 858,625 1082,625 1100,650" fill="var(--blue-top)"/>
    <polygon points="1118,650 1100,625 1310,625 1388,650" fill="var(--grey-top)"/>
    <rect x="540" y="650" width="270" height="64" fill="var(--orange)"/>
    <rect x="830" y="650" width="270" height="64" fill="var(--blue)"/>
    <rect x="1118" y="650" width="270" height="64" fill="var(--grey)"/>
    <text class="tier-label block-label" x="670" y="689">Vulnerability Management</text>
    <text class="tier-label block-label" x="964" y="679">24x7</text>
    <text class="tier-label block-label" x="964" y="698">Continuous Detection &amp; Response</text>
    <text class="tier-label block-label" x="1254" y="689">Governance, Risk &amp; Compliance</text>
  </g>
</svg>
</body>
</html>
```